Toward Bright Morrow (TWBM) Business Card - company with a mission

Note* The file attached... orange with "Toward Bright MORROW" (in CAPS) is our logo. I am also open to having the text "toward bright morrow" OUTSIDE the orange round logo for business card (so yes, you may take the text out).

The info: (the following info are separate. So either you can use Martin or Helena for now, but that will be 2 separate cards, not together in one card. Thanks!!

Martin K Pardo
202.555.0183
martin@towardbrightmorrow.example
Managing Partner

Helena R Voss
202.555.0147
helena@towardbrightmorrow.example
Managing Partner

Our website: www.towardbrightmorrow.example

TWBM LLC stands for Toward Bright Morrow (non profit arm is called dawn lift foundation)—our business is based out of New York City and has a non-profit arm where for every bar of soap you purchase, we donate a bar (don’t want any designs that limits us to only soap). Currently working with South Africa. We want the focus to be organic/natural soap with a mission.

Looking for a clean, fresh design.

Industry/Entity Type

Non-Profit

Requirements
Must have
• Clean, fresh, refreshing. Design should not be too busy.

```html
<!DOCTYPE html>
<html lang="en">
<head>
<meta charset="utf-8">
<title>Toward Bright Morrow – Business Card</title>
<link rel="stylesheet" href="https://fonts.googleapis.com/css2?family=Open+Sans:wght@400;600;700&display=swap">
<style>
  :root {
    --backdrop: #1d1d1e;
    --card-brown: #3e302d;
    --kraft: #c59a62;
    --logo-orange: #f1a96a;
    --gold-text: #dcaa5e;
    --logo-ink: #ffffff;
    --faint-orange: rgba(241, 169, 106, 0.55);
  }
  * { margin: 0; padding: 0; box-sizing: border-box; }
  html, body {
    width: 1200px; height: 1000px; overflow: hidden;
    background: var(--backdrop);
    font-family: "Open Sans", Arial, sans-serif;
  }
  .canvas { position: relative; width: 1200px; height: 1000px; }

  .card {
    position: absolute; width: 700px; height: 400px;
    background: var(--card-brown); overflow: hidden;
    box-shadow: 0 14px 30px rgba(0,0,0,0.55);
  }
  .card--back  { left: 150px; top: 70px; }
  .card--front { left: 350px; top: 530px; }

  .kraft-band {
    position: absolute; left: 0; top: 0; bottom: 0; width: 120px;
    background: var(--kraft);
  }

  .logo-badge {
    position: absolute; border-radius: 50%;
    background: var(--logo-orange);
    display: flex; align-items: center; justify-content: center;
    color: var(--logo-ink); font-weight: 700; letter-spacing: 1px;
  }
  .card--back .logo-badge { width: 170px; height: 150px; left: 320px; top: 70px; font-size: 40px; }
  .card--front .logo-badge { width: 140px; height: 124px; left: 50px; top: 50px; font-size: 32px; }

  .back-website {
    position: absolute; left: 120px; right: 0; top: 260px;
    text-align: center; color: var(--gold-text);
    font-weight: 700; font-size: 21px; letter-spacing: 0.3px;
  }

  .faint-circle {
    position: absolute; width: 330px; height: 330px; border-radius: 50%;
    right: -110px; top: -50px; background: var(--faint-orange);
  }

  .identity { position: absolute; left: 215px; top: 62px; color: var(--gold-text); }
  .identity__name {
    font-weight: 700; font-size: 29px; letter-spacing: 0.5px;
    padding-bottom: 2px; border-bottom: 2px solid var(--gold-text);
  }
  .identity__role { font-weight: 600; font-size: 18px; letter-spacing: 2.5px; margin-top: 2px; padding-left: 10px; }

  .contact-list { position: absolute; left: 228px; top: 215px; list-style: none; color: var(--gold-text); }
  .contact-list li { display: flex; align-items: center; gap: 12px; font-size: 20px; line-height: 34px; }
  .contact-list svg { width: 16px; height: 16px; fill: none; stroke: var(--gold-text); stroke-width: 1.8; }
</style>
</head>
<body>
<main class="canvas">
  <section class="card card--back" aria-label="Business card back">
    <div class="kraft-band"></div>
    <div class="logo-badge">TWBM</div>
    <p class="back-website">www.towardbrightmorrow.example</p>
  </section>

  <section class="card card--front" aria-label="Business card front">
    <div class="kraft-band"></div>
    <div class="faint-circle"></div>
    <div class="logo-badge">TWBM</div>
    <div class="identity">
      <h1 class="identity__name">Martin K Pardo</h1>
      <p class="identity__role">Managing Partner</p>
    </div>
    <ul class="contact-list">
      <li>
        <svg viewBox="0 0 16 16" aria-hidden="true"><rect x="4" y="1.5" width="8" height="13" rx="1.5"/><line x1="7" y1="12" x2="9" y2="12"/></svg>
        202.555.0183
      </li>
      <li>
        <svg viewBox="0 0 16 16" aria-hidden="true"><rect x="1.5" y="3.5" width="13" height="9"/><polyline points="1.5,3.5 8,9 14.5,3.5"/></svg>
        martin@towardbrightmorrow.example
      </li>
      <li>
        <svg viewBox="0 0 16 16" aria-hidden="true"><rect x="1" y="6" width="8" height="4" rx="2" transform="rotate(-45 5 8)"/><rect x="7" y="6" width="8" height="4" rx="2" transform="rotate(-45 11 8)"/></svg>
        www.towardbrightmorrow.example
      </li>
    </ul>
  </section>
</main>
</body>
</html>
```